Online Home Automation business needs business card design

New business starting up that sells home-automation products in Australia. Business card needs to look very polished and professional. The business name is "Vesk Automation".
Updates

Thank you all for the great designs, We are really impressed. We are in the process of deciding on a design but keep the designs coming in.

Industry/Entity Type

Business

```html
<!DOCTYPE html>
<html lang="en">
<head>
<meta charset="utf-8">
<title>Vesk Automation — Business Card</title>
<link rel="stylesheet" href="https://fonts.googleapis.com/css2?family=Arimo:wght@400;700&display=swap">
<style>
  :root {
    --backdrop: #d6d7db;
    --card-grey: #bdbdbd;
    --brand-red: #e8232a;
    --ink: #151515;
    --white: #ffffff;
    --rule: #8a8a8a;
  }
  * { box-sizing: border-box; margin: 0; padding: 0; }
  html, body {
    width: 1200px;
    height: 960px;
    overflow: hidden;
    background: var(--backdrop);
    font-family: "Arimo", Arial, sans-serif;
  }
  .canvas {
    position: relative;
    width: 1200px;
    height: 960px;
  }
  .card {
    position: absolute;
    top: 320px;
    width: 530px;
    height: 310px;
    box-shadow: 0 6px 18px rgba(0,0,0,0.18);
    overflow: hidden;
  }

  /* Front side */
  .card-front {
    left: 55px;
    background: var(--card-grey);
  }
  .brand-lockup {
    position: absolute;
    left: 34px;
    top: 44px;
    display: flex;
    align-items: center;
  }
  .brand-dot {
    width: 58px;
    height: 58px;
    border-radius: 50%;
    background: var(--ink);
  }
  .brand-divider {
    width: 1px;
    height: 58px;
    background: var(--rule);
    margin: 0 14px;
  }
  .brand-name {
    font-weight: 400;
    font-size: 38px;
    letter-spacing: -1px;
    color: var(--ink);
    margin-top: 46px;
  }
  .front-web {
    position: absolute;
    left: 34px;
    bottom: 64px;
    font-size: 13px;
    color: var(--ink);
  }
  .front-web .accent { color: var(--brand-red); }
  .contact-block {
    position: absolute;
    right: 34px;
    bottom: 40px;
    text-align: right;
  }
  .person-name {
    font-size: 26px;
    color: var(--brand-red);
    margin-bottom: 16px;
    letter-spacing: 0.5px;
  }
  .person-name .first { font-weight: 700; }
  .person-name .last { font-weight: 400; }
  .contact-line {
    font-size: 14px;
    color: var(--ink);
    line-height: 1.3;
  }

  /* Back side */
  .card-back {
    left: 615px;
    background: var(--brand-red);
  }
  .back-web {
    position: absolute;
    left: 36px;
    top: 50%;
    transform: translate(-50%, -50%) rotate(90deg) translateY(-50%);
    transform-origin: center;
    font-size: 14px;
    color: var(--ink);
    white-space: nowrap;
  }
  .back-web .accent { color: var(--white); }
  .back-lockup {
    position: absolute;
    left: 50%;
    top: 50%;
    transform: translate(-45%, -50%);
    display: flex;
    align-items: center;
    gap: 14px;
  }
  .back-lockup .brand-dot {
    width: 46px;
    height: 46px;
  }
  .back-lockup .brand-name {
    margin-top: 0;
    font-size: 32px;
  }
</style>
</head>
<body>
<main class="canvas">
  <section class="card card-front" aria-label="Business card front">
    <div class="brand-lockup">
      <span class="brand-dot" aria-hidden="true"></span>
      <span class="brand-divider" aria-hidden="true"></span>
      <span class="brand-name">Vesk Automation</span>
    </div>
    <p class="front-web">www.<span class="accent">veskautomation</span>.com.au</p>
    <div class="contact-block">
      <p class="person-name"><span class="first">MARCUS</span> <span class="last">HALE</span></p>
      <p class="contact-line">+61 400 555 219</p>
      <p class="contact-line">info@veskautomation.com.au</p>
    </div>
  </section>

  <section class="card card-back" aria-label="Business card back">
    <p class="back-web">www.<span class="accent">veskautomation</span>.com.au</p>
    <div class="back-lockup">
      <span class="brand-dot" aria-hidden="true"></span>
      <span class="brand-name">Vesk Automation</span>
    </div>
  </section>
</main>
</body>
</html>
```